依頼詳細
珪藻土バスマットを販売するにあたり、店舗にチラシを設置しようと思います。そのチラシ制作をお願いします。同種製品が多いので明るくおしゃれでわかりやすいデザインを望んでいます。
以前使用していたデモチラシがあるので内容は同じでデザインをかっこよくしてほしいです。
記載項目
キャッチコピー、製品名、特徴、製品写真
※以前使っていたもののデモチラシがあるので基本的に文言などはそちらを参照してください。デモにある文言は必須で入れてください。その他に必要なものがあれば提案で掲載していただいたOKです。
サイズ
A4
ページ数
片面
希望イメージ
シンプル 複雑
単色 カラフル
暗い 明るい
日常 高級
遊び心 厳粛
未来的 伝統的
女性的 男性的
希望する色
納品ファイル
• イラストレーター形式 (.ai)
補足説明
イラストレーターで元データとアウトラインデータを下さい。
関連書類の添付忘れを追加しました。
■ 選んだ理由

関係者の多数決で、メインターゲットとなる女性に人気があったため選ばせていただきました。

■ 提案者全員のお礼・コメント

みなさん非常に素敵なデザインで本当に迷いました。せっかく作っていただいてもったいないのですが、今回は関係者の多数決で1点に絞らせていただきました。

提案くださった皆様ありがとうございました!

```html
<!DOCTYPE html>
<html lang="ja">
<head>
<meta charset="UTF-8">
<title>快適ソヨカゼマット</title>
<link rel="stylesheet" href="https://fonts.googleapis.com/css2?family=M+PLUS+Rounded+1c:wght@500;800&family=Noto+Sans+JP:wght@400;700;900&display=swap">
<style>
  :root{
    --blue:#1d7fd1;
    --blue-dark:#0e4f98;
    --navy:#1a2f6b;
    --sky:#e8f4fc;
    --sky-mid:#c9e4f6;
    --pink:#ec5f9a;
    --green:#3fae4a;
    --orange:#f39a1e;
    --red:#d9241f;
    --ink:#333;
    --white:#fff;
  }
  *{margin:0;padding:0;box-sizing:border-box}
  html,body{width:846px;height:1200px;overflow:hidden;background:var(--white)}
  body{font-family:"Noto Sans JP",sans-serif;color:var(--ink)}
  .flyer{position:relative;width:846px;height:1200px;overflow:hidden;
    background:radial-gradient(ellipse at 20% 90%,var(--sky) 0,transparent 55%),
               radial-gradient(ellipse at 85% 60%,var(--sky) 0,transparent 50%),var(--white)}
  .catch-band{position:absolute;left:0;top:0;width:846px;height:100px;
    background:linear-gradient(90deg,var(--blue-dark),var(--blue) 50%,var(--blue-dark));
    display:flex;align-items:center;justify-content:center}
  .catch{font-family:"M PLUS Rounded 1c",sans-serif;font-weight:800;font-size:52px;color:var(--white);
    letter-spacing:2px;text-shadow:0 3px 0 rgba(0,0,0,.18)}
  .scene-photo{position:absolute;left:430px;top:100px;width:416px;height:470px;
    background:linear-gradient(160deg,#f3f6f9 0%,#dfe7ee 55%,#c8d3dd 100%)}
  .easy-badge{position:absolute;left:448px;top:118px;width:92px;height:92px;border-radius:50%;
    background:var(--blue);color:var(--white);font-weight:700;font-size:15px;line-height:1.25;
    display:flex;align-items:center;justify-content:center;text-align:center;transform:rotate(-12deg)}
  .quick-dry{position:absolute;left:600px;top:140px;color:var(--blue);font-weight:700;font-size:22px;line-height:1.4;text-align:center}
  .quick-dry strong{display:block;font-size:40px;font-weight:900;color:var(--blue)}
  .product-name{position:absolute;left:40px;top:150px;font-family:"M PLUS Rounded 1c",sans-serif;font-weight:800;line-height:1}
  .product-name span{display:block}
  .name-top{font-size:88px;color:var(--navy);padding-left:90px;letter-spacing:6px}
  .name-main{font-size:104px;color:var(--blue);margin-top:26px;letter-spacing:-2px;
    text-shadow:3px 3px 0 var(--white),5px 5px 0 var(--sky-mid)}
  .name-sub{font-size:56px;color:var(--navy);margin-top:18px;padding-left:110px;letter-spacing:10px}
  .features{position:absolute;left:96px;top:580px;display:flex;gap:12px;list-style:none}
  .features li{width:70px;height:70px;border-radius:50%;color:var(--white);font-weight:700;font-size:15px;
    display:flex;align-items:center;justify-content:center;text-align:center;line-height:1.1;border:3px solid var(--white);
    box-shadow:0 2px 4px rgba(0,0,0,.15)}
  .f-dry{background:var(--blue)} .f-mold{background:var(--pink)} .f-odor{background:var(--green)} .f-natural{background:var(--orange)}
  .product-photo{position:absolute;left:110px;top:680px;width:626px;height:250px;border-radius:6px;
    background:linear-gradient(170deg,#f4f4f2 0%,#e6e7e6 60%,#d4d7da 100%)}
  .headline{position:absolute;left:0;width:846px;top:965px;text-align:center;font-weight:900;font-size:30px;color:var(--navy)}
  .headline em{font-style:normal;color:var(--blue)}
  .headline::after{content:"";display:block;width:760px;height:3px;margin:6px auto 0;background:linear-gradient(90deg,transparent,var(--blue),transparent)}
  .body-copy{position:absolute;left:50px;top:1020px;width:746px;font-size:13px;line-height:1.7;color:var(--ink)}
  .absorb{position:absolute;left:40px;top:1100px;width:90px;height:90px;border-radius:50%;background:var(--white);
    border:3px solid var(--blue);color:var(--blue);font-weight:900;font-size:17px;line-height:1.2;
    display:flex;align-items:center;justify-content:center;text-align:center}
  .absorb-steps{position:absolute;left:150px;top:1100px;width:490px;height:90px;border:2px solid var(--sky-mid);border-radius:8px;background:var(--white)}
  .absorb-caption{position:absolute;left:0;top:4px;width:100%;text-align:center;font-size:13px;color:var(--blue);font-weight:700}
  .step-row{position:absolute;left:14px;top:28px;display:flex;align-items:center;gap:8px}
  .step{width:135px;height:52px;border-radius:4px;background:linear-gradient(180deg,#d7dde3,#b5c0ca)}
  .made-in{position:absolute;left:680px;top:1110px;width:130px;height:60px;border:3px solid var(--red);color:var(--red);
    font-weight:900;font-size:30px;display:flex;align-items:center;justify-content:center;background:var(--white)}
</style>
</head>
<body>
<main class="flyer">
  <header class="catch-band"><h2 class="catch">乗った瞬間からみるみる吸水!</h2></header>

  <div class="scene-photo" role="img" aria-label="白いバスマットに素足で乗っている足元の写真"></div>
  <div class="easy-badge">お手入れ<br>簡単!</div>
  <p class="quick-dry">何回乗っても<br>すぐに<strong>サラサラ!</strong></p>

  <h1 class="product-name">
    <span class="name-top">快適</span>
    <span class="name-main">ソヨカゼ</span>
    <span class="name-sub">マット</span>
  </h1>

  <ul class="features">
    <li class="f-dry">速乾</li>
    <li class="f-mold">防カビ</li>
    <li class="f-odor">消臭</li>
    <li class="f-natural">天然<br>素材</li>
  </ul>

  <div class="product-photo" role="img" aria-label="白いバスマット製品の写真"></div>

  <h3 class="headline"><em>バーミキュライト</em>と<em>珪藻土</em>を配合した多機能新素材!</h3>
  <p class="body-copy">珪藻土マットより吸水力にすぐれたバーミキュライトを主材に使用した快適ソヨカゼマットです。多孔質の素材が足裏の水分をすばやく吸い取り、表面はすぐに乾きます。カビやにおいの発生も抑えるので、毎日清潔にお使いいただけます。</p>

  <div class="absorb">抜群の<br>吸水力</div>
  <div class="absorb-steps">
    <p class="absorb-caption">足の裏の水分をすばやく吸い取ります</p>
    <div class="step-row">
      <div class="step" role="img" aria-label="濡れた足跡が付いたマット"></div>
      <svg width="12" height="20" viewBox="0 0 12 20"><path d="M2 2l8 8-8 8" fill="none" stroke="#1d7fd1" stroke-width="3"/></svg>
      <div class="step" role="img" aria-label="足跡が薄くなっていくマット"></div>
      <svg width="12" height="20" viewBox="0 0 12 20"><path d="M2 2l8 8-8 8" fill="none" stroke="#1d7fd1" stroke-width="3"/></svg>
      <div class="step" role="img" aria-label="乾いたマット"></div>
    </div>
  </div>
  <div class="made-in">日本製</div>
</main>
</body>
</html>
```